依頼詳細
PCとスマホデザインの両方納品をいただきますが、
まずはデザインイメージが確認しやすいPCページのみの提案をお願いします。
スマホページは当選者に納品時にお願いしたいと思います。
スマホサイズについて、表示は横幅375pxで作成し、
デザインデータは2倍の横幅750pxのカンバスサイズで作成してください。
(Retinaディスプレイに対応するため)
レスポンシブウェブデザインを意識したデザインでお願いします。

■サイトマップ
添付の画面遷移図をご確認ください。

■参考サイト
https://www.kurumi-p.co.jp/
https://www.m-sorano.co.jp/
https://www.fujino-printing.co.jp/

■内容について
印刷会社のサイトリニューアルになります。
既存サイト
https://www.hinata-printing.co.jp/

■素材写真
画像データについては、フリー素材から流用して
イメージ画像に当て込んでください。
足りない場合は、一旦他のサイトの写真をサンプルとして
入れてください。(サンプルなどの表記をお願いします)
また、購入が必要な写真などを利用した場合、
価格とサイト名を教えてください。

また、Pixmora Stockで定期契約をしていますので、
Pixmora Stockの画像は使用できます。
デザイン時はカンプ画像をお入れいただきますようお願いします。

※採用サイト寄りのサイトにしたいので、使用する画像は
なるべく人物が入っているものを使用してください。

■ワイヤーフレーム
https://mock.plavetta.jp/view/51830427-216b-4c73-9a05-87162534907e-4182/?fullscreen
コンテンツの構成としてワイヤーフレームを作成しましたが
必ずしもワイヤーフレームの通りではなくて大丈夫です。
TOPページに配置するコンテンツを見ていただき、デザインは
デザイナーの皆様におまかせしたいと思います。

----------------------------------------------------------------------------
【制作物に対するお願い】

■フォントについて
・無料で使えるフォントで作成をお願いします。
・OSに紐づくフォントの使用は控えていただければと思います (ヒラギノなど)

ページ数
1ページ
希望イメージ
シンプル 複雑
単色 カラフル
暗い 明るい
日常 高級
遊び心 厳粛
未来的 伝統的
女性的 男性的
希望する色
青系、既存サイトに載っているロゴのイメージでお願いします。
納品ファイル
• 高解像度JPG (.jpg)
• イラストレーター形式 (.ai)
• フォトショップ形式 (.psd)
補足説明
上記のいずれか1つ(アウトラインありとなしの2つ)と高解像度JPGを納品お願いします。
adobe XDでの納品も可能です。

```html
<!DOCTYPE html>
<html lang="ja">
<head>
<meta charset="utf-8">
<title>ヒナタ印刷 | POWER TO CREATE</title>
<link rel="stylesheet" href="https://fonts.googleapis.com/css2?family=Montserrat:wght@500;600;700;800&family=Noto+Sans+JP:wght@400;500;700;900&display=swap">
<style>
:root{
  --blue:#1c90d6;
  --blue-deep:#1576b3;
  --ink:#222831;
  --muted:#6b7178;
  --line:#e3e6ea;
  --pale:#f3f4f6;
  --white:#ffffff;
}
*{margin:0;padding:0;box-sizing:border-box}
html,body{width:1200px;height:3928px;overflow:hidden}
body{font-family:"Noto Sans JP",sans-serif;color:var(--ink);background:var(--white);position:relative}
.photo{display:block}
.btn{display:inline-flex;align-items:center;justify-content:center;width:130px;height:34px;border-radius:17px;background:var(--blue);color:#fff;font:700 12px "Montserrat",sans-serif;letter-spacing:.08em;text-decoration:none}
.btn--white{background:#fff;color:var(--blue)}
.sec-title{font:700 52px/1 "Montserrat",sans-serif;color:var(--ink)}
.sec-sub{font-size:12px;color:var(--blue);font-weight:700;margin-top:8px}

/* header + hero */
.hero{position:absolute;left:0;top:0;width:1200px;height:780px}
.hero__photo{position:absolute;inset:0;background:linear-gradient(115deg,#3b4452 0%,#8a8f96 30%,#d9c9a8 55%,#4fa3c9 75%,#c84f6a 100%)}
.hero__shade{position:absolute;inset:0;background:linear-gradient(90deg,rgba(10,20,35,.55),rgba(10,20,35,.1))}
.header{position:absolute;left:0;top:0;width:1200px;height:92px;background:rgba(255,255,255,.96);display:flex;align-items:center;padding:0 40px 0 110px}
.brand{display:flex;align-items:center;gap:10px;font-weight:900;font-size:22px;color:var(--blue-deep)}
.brand__mark{width:22px;height:22px;background:var(--blue)}
.nav{margin-left:auto;display:flex;align-items:center;gap:34px;font-size:13px;font-weight:500}
.nav .btn{width:120px;height:36px}
.hero__copy{position:absolute;left:70px;top:150px;color:#fff}
.hero__title{font:800 132px/.93 "Montserrat",sans-serif;letter-spacing:.01em}
.hero__lead{font-size:30px;font-weight:700;margin-top:26px;letter-spacing:.05em}

/* concept */
.concept{position:absolute;left:0;top:780px;width:1200px;height:600px}
.concept__ghost{position:absolute;left:70px;top:70px;font:700 82px "Montserrat",sans-serif;color:#eceef0}
.concept__head{position:absolute;left:70px;top:120px;font-size:28px;font-weight:900;line-height:1.45}
.concept__body{position:absolute;left:70px;top:232px;width:470px;font-size:12px;line-height:2.05;color:#444}
.concept__body p+p{margin-top:16px}
.concept__photo{position:absolute;left:600px;top:-20px;width:600px;height:572px;background:linear-gradient(135deg,#7c4b2e,#d8a04a 40%,#c9c2b3 65%,#2f3a46)}

/* service */
.service{position:absolute;left:0;top:1440px;width:1200px;height:500px}
.service__photo{position:absolute;left:0;top:0;width:840px;height:440px;background:linear-gradient(120deg,#2b3640,#5d6e73 40%,#3fbf8e 70%,#e8eef0)}
.service__card{position:absolute;left:600px;top:60px;width:600px;height:420px;background:var(--pale);padding:80px 60px}
.service__card .sec-title{font-size:56px}
.service__text{font-size:12px;line-height:2.1;color:#444;margin:30px 0 36px}

/* work */
.work{position:absolute;left:0;top:1980px;width:1200px;height:500px}
.work__head{position:absolute;left:80px;top:0}
.work__list{position:absolute;left:80px;top:120px;display:flex;gap:24px}
.work-card{width:244px;height:240px;background:#fff;box-shadow:0 2px 10px rgba(0,0,0,.1)}
.work-card__img{height:130px;background:linear-gradient(135deg,#e9ecef,#cfd6dc 50%,#f5f5f5)}
.work-card__txt{padding:14px 16px;font-size:12px;line-height:1.8}
.work-card__tag{font-size:10px;color:var(--muted);margin-top:8px}
.work .btn{position:absolute;left:535px;top:412px}

/* banners */
.banners{position:absolute;left:80px;top:2540px;width:1040px;height:240px}
.banner{position:absolute;top:0;height:240px;text-decoration:none}
.banner--company{left:0;width:560px;background:linear-gradient(120deg,#0d4f8c,#2a86c8);clip-path:polygon(0 0,100% 0,92% 100%,0 100%)}
.banner--draft{right:0;width:530px}
.banner__bg{position:absolute;inset:0;background:linear-gradient(135deg,#d8ebf7 0%,#eef4f8 45%,#f4f7f9 70%,#cfe6f4 100%)}
.banner__title{position:absolute;font:700 30px/1 "Montserrat",sans-serif}
.banner__sub{position:absolute;font-size:11px;font-weight:700}

/* news */
.news{position:absolute;left:0;top:2880px;width:1200px;height:280px}
.news__head{position:absolute;left:80px;top:20px}
.news .btn{position:absolute;left:80px;top:176px}
.news__list{position:absolute;left:340px;top:30px;width:780px;list-style:none}
.news__item{display:flex;align-items:center;height:80px;border-bottom:1px solid var(--line);padding:0 20px;font-size:13px;background:#fafbfc;margin-bottom:12px}
.news__date{font:500 12px "Montserrat",sans-serif;color:var(--muted);width:110px}
.news__arrow{margin-left:auto}

/* blog */
.blog{position:absolute;left:0;top:3200px;width:1200px;height:340px;background:var(--blue-deep)}
.blog .sec-title{color:#fff}
.blog .sec-sub{color:#fff}
.blog__head{position:absolute;left:80px;top:80px}
.blog .btn{position:absolute;left:80px;top:196px}
.blog__list{position:absolute;left:340px;top:80px;display:flex;gap:30px}
.blog-card{width:240px;background:#fff}
.blog-card__img{height:120px;background:linear-gradient(135deg,#8aa2b4,#d7dde2)}
.blog-card__txt{padding:10px 14px 14px;font-size:11px;line-height:1.6}
.blog-card__date{font:500 10px "Montserrat",sans-serif;color:var(--muted)}

/* footer */
.footer{position:absolute;left:0;top:3540px;width:1200px;height:388px;text-align:center}
.footer .brand{justify-content:center;margin-top:70px}
.footer__addr{font-size:11px;line-height:1.9;color:#444;margin-top:18px}
.footer__links{font-size:10px;color:#555;margin-top:34px;display:flex;justify-content:center;gap:26px}
.footer__copy{font:500 9px "Montserrat",sans-serif;color:var(--muted);margin-top:56px}
</style>
</head>
<body>

<section class="hero">
  <div class="hero__photo photo" role="img" aria-label="カラーチャートを確認する人の手元の写真"></div>
  <div class="hero__shade"></div>
  <header class="header">
    <div class="brand"><span class="brand__mark"></span>ヒナタ印刷</div>
    <nav class="nav">
      <span>業務案内</span><span>入稿について</span><span>事業紹介</span><span>会社概要</span>
      <a class="btn" href="#">CONTACT</a>
    </nav>
  </header>
  <div class="hero__copy">
    <h1 class="hero__title">POWER<br>TO<br>CREATE</h1>
    <p class="hero__lead">お客様に最適な印刷メディアを</p>
  </div>
</section>

<section class="concept">
  <div class="concept__ghost">Concept</div>
  <h2 class="concept__head">ヒナタ印刷は<br>お客様と共に考えます。</h2>
  <div class="concept__body">
    <p>創業以来、印刷物を通じてお客様の想いを形にしてきました。企画から制作、印刷、加工、発送まで一貫して対応し、目的に合わせた最適な印刷メディアをご提案いたします。</p>
    <p>私たちは「何を必要としているのか」を第一に考え、お客様と同じ目線で課題に向き合います。確かな技術と柔軟な発想で、これからも地域と共に歩み続けてまいります。</p>
  </div>
  <div class="concept__photo photo" role="img" aria-label="パッケージや冊子など印刷物が並ぶ写真"></div>
</section>

<section class="service">
  <div class="service__photo photo" role="img" aria-label="大判プリンターで出力物を扱う手元の写真"></div>
  <div class="service__card">
    <h2 class="sec-title">Service</h2>
    <p class="sec-sub">業務案内</p>
    <p class="service__text">ヒナタ印刷では、お客様の企画に合ったチョイスができるよう、<br>多数の設備を揃えております。<br>企画からデータ作成、印刷、加工までご相談ください。</p>
    <a class="btn" href="#">MORE</a>
  </div>
</section>

<section class="work">
  <div class="work__head"><h2 class="sec-title">Work</h2><p class="sec-sub">事業紹介</p></div>
  <div class="work__list">
    <article class="work-card"><div class="work-card__img photo" role="img" aria-label="印刷物の事例写真"></div><div class="work-card__txt">ダミーテキストです。フォントサイズ、文字並びなどの確認用です。<p class="work-card__tag">印刷物の事例</p></div></article>
    <article class="work-card"><div class="work-card__img photo" role="img" aria-label="印刷物の事例写真"></div><div class="work-card__txt">ダミーテキストです。フォントサイズ、文字並びなどの確認用です。<p class="work-card__tag">印刷物の事例</p></div></article>
    <article class="work-card"><div class="work-card__img photo" role="img" aria-label="印刷物の事例写真"></div><div class="work-card__txt">ダミーテキストです。フォントサイズ、文字並びなどの確認用です。<p class="work-card__tag">印刷物の事例</p></div></article>
    <article class="work-card"><div class="work-card__img photo" role="img" aria-label="印刷物の事例写真"></div><div class="work-card__txt">ダミーテキストです。フォントサイズ、文字並びなどの確認用です。<p class="work-card__tag">印刷物の事例</p></div></article>
  </div>
  <a class="btn" href="#">MORE</a>
</section>

<section class="banners">
  <a class="banner banner--company" href="#">
    <span class="photo" role="img" aria-label="オフィスビルの写真" style="position:absolute;inset:0"></span>
    <span class="banner__title" style="left:180px;top:100px;color:#fff">Company</span>
    <span class="banner__sub" style="left:180px;top:144px;color:#fff">会社概要</span>
  </a>
  <a class="banner banner--draft" href="#">
    <span class="banner__bg" role="img" aria-label="青系の幾何学模様の装飾背景"></span>
    <span class="banner__title" style="left:180px;top:96px;color:var(--ink)">Draft Data</span>
    <span class="banner__sub" style="left:180px;top:140px;color:var(--blue)">データ入稿について</span>
  </a>
</section>

<section class="news">
  <div class="news__head"><h2 class="sec-title">News</h2><p class="sec-sub">新着情報</p></div>
  <a class="btn" href="#">MORE</a>
  <ul class="news__list">
    <li class="news__item"><span class="news__date">2021.08.22</span>ダミーテキストです。フォントサイズ、文字量、文字並びなどの確認用です。<svg class="news__arrow" width="8" height="12"><path d="M1 1l5 5-5 5" stroke="#1c90d6" stroke-width="2" fill="none"/></svg></li>
    <li class="news__item"><span class="news__date">2021.08.22</span>ダミーテキストです。フォントサイズ、文字量、文字並びなどの確認用です。<svg class="news__arrow" width="8" height="12"><path d="M1 1l5 5-5 5" stroke="#1c90d6" stroke-width="2" fill="none"/></svg></li>
    <li class="news__item"><span class="news__date">2021.08.22</span>ダミーテキストです。フォントサイズ、文字量、文字並びなどの確認用です。<svg class="news__arrow" width="8" height="12"><path d="M1 1l5 5-5 5" stroke="#1c90d6" stroke-width="2" fill="none"/></svg></li>
  </ul>
</section>

<section class="blog">
  <div class="blog__head"><h2 class="sec-title">Blog</h2><p class="sec-sub">ブログ</p></div>
  <a class="btn btn--white" href="#">MORE</a>
  <div class="blog__list">
    <article class="blog-card"><div class="blog-card__img photo" role="img" aria-label="社内研修の集合写真"></div><div class="blog-card__txt"><p class="blog-card__date">2021.08.22</p>社内研修を行いました</div></article>
    <article class="blog-card"><div class="blog-card__img photo" role="img" aria-label="会議室での説明会の写真" style="background:linear-gradient(135deg,#c9d3da,#6f8799)"></div><div class="blog-card__txt"><p class="blog-card__date">2021.08.22</p>会社説明会を開催</div></article>
    <article class="blog-card"><div class="blog-card__img photo" role="img" aria-label="駐車場の案内看板の写真" style="background:linear-gradient(135deg,#e4e8ec,#3a6fb0)"></div><div class="blog-card__txt"><p class="blog-card__date">2021.08.22</p>新しい駐車場のご案内</div></article>
  </div>
</section>

<footer class="footer">
  <div class="brand"><span class="brand__mark"></span>ヒナタ印刷</div>
  <p class="footer__addr">〒000-0000 架空県みどり市ひなた町1丁目2番3号<br>TEL 000-000-0000　FAX 000-000-0001</p>
  <div class="footer__links"><span>お問い合わせ</span><span>プライバシーポリシー</span><span>サイトマップ</span></div>
  <p class="footer__copy">© HINATA PRINTING</p>
</footer>

</body>
</html>
```